INCOME TAX SERVIES AMERICAN THEME

SOMETHING SIMILAR TO IMAGE IM PROVIDING NOT SURE IF ITS NEEDS TO BE CODED OR UNCODED I JUST NEED IT TO WORK WITH WEEBLY.

Industry/Entity Type

Work

Coding

Coded - Design and coding required

Number of Pages Required

5+ page

Colors
0355a3
ffffff
ec1f27

Requirements
Must have
• MUST BE COMPATIBLE WITH WEEBLY
Nice to have
• WOULD LIKE THE FOOTER TO SIMILAR TO PIXELHARBOR PAGE.

```html
<!DOCTYPE html>
<html lang="en">
<head>
<meta charset="utf-8">
<title>Liberty Ledger Tax</title>
<link href="https://fonts.googleapis.com/css2?family=Open+Sans:wght@400;600;700;800&display=swap" rel="stylesheet">
<style>
:root{
  --blue:#0355a3;
  --blue-dark:#023f7a;
  --red:#ec1f27;
  --white:#ffffff;
  --ink:#333a44;
  --muted:#7a828c;
  --line:#dfe3e8;
  --footer:#2b3038;
  --footer-bottom:#1f2329;
  --page:#f4f5f7;
}
*{box-sizing:border-box;margin:0;padding:0}
html,body{width:709px;height:1200px;overflow:hidden}
body{font-family:"Open Sans",Arial,sans-serif;color:var(--ink);background:var(--white);font-size:6px;line-height:1.5}
.page{position:relative;width:709px;height:1200px}

/* header */
.site-header{position:absolute;left:0;top:0;width:709px;height:66px;background:var(--white);border-top:3px solid var(--blue)}
.brand{position:absolute;left:26px;top:10px;display:flex;align-items:center;gap:6px}
.brand-mark{width:16px;height:16px;background:var(--red)}
.brand-name{font-weight:800;font-size:19px;line-height:1;color:var(--blue);letter-spacing:.2px;width:150px}
.top-contact{position:absolute;right:22px;top:8px;display:flex;align-items:center;gap:4px;font-size:8px;color:var(--ink)}
.top-contact svg{margin-right:2px}
.social-dot{width:11px;height:11px;background:var(--red);border-radius:2px}
.main-nav{position:absolute;right:0;top:30px;width:440px;height:16px;background:var(--blue);display:flex;justify-content:space-around;align-items:center}
.main-nav a{color:var(--white);text-decoration:none;font-size:6px;font-weight:700;letter-spacing:.3px}
.main-nav a.active{background:var(--red);padding:4px 8px}

/* hero */
.hero{position:absolute;left:0;top:50px;width:709px;height:220px;background:linear-gradient(120deg,#cfd6df 0%,#9fb0c4 45%,#5f7590 100%)}
.hero-welcome{position:absolute;left:96px;top:60px;width:240px;background:rgba(255,255,255,.94);padding:10px 12px}
.hero-welcome h1{font-size:13px;font-weight:800;color:var(--blue);line-height:1.1}
.hero-welcome h1 span{display:block;color:var(--red);font-size:17px}
.hero-welcome p{margin-top:6px;font-size:5.5px;color:var(--muted)}
.hero-arrow{position:absolute;top:100px;width:16px;height:22px;display:flex;align-items:center;justify-content:center}
.hero-arrow.prev{left:90px}.hero-arrow.next{right:86px}

/* feature boxes */
.features{position:absolute;left:122px;top:258px;width:466px;height:140px;display:flex;gap:6px}
.feature{flex:1;position:relative;background:var(--white);box-shadow:0 2px 6px rgba(0,0,0,.15)}
.feature-photo{position:absolute;inset:0 0 30px 0}
.feature-caption{position:absolute;left:0;right:0;bottom:0;height:30px;background:var(--red);color:var(--white);padding:5px 8px;font-weight:700;font-size:7px}
.feature-caption small{display:block;font-weight:400;font-size:5px}
.feature.is-blue{background:var(--blue);color:var(--white);text-align:center;padding-top:18px}
.feature.is-blue h3{font-size:8px;font-weight:700;margin-top:6px}
.feature.is-blue p{font-size:5px;padding:4px 14px}
.btn{display:inline-block;background:var(--red);color:var(--white);font-size:5.5px;font-weight:700;padding:3px 9px;border-radius:2px}
.btn.dark{background:var(--blue-dark)}

/* what we do */
.what-we-do{position:absolute;left:122px;top:415px;width:466px;height:170px}
.wwd-photo{position:absolute;left:0;top:0;width:220px;height:150px;background:linear-gradient(135deg,#d9d2c8,#8d8f98 60%,#4f5766)}
.wwd-text{position:absolute;left:232px;top:0;width:234px}
.section-title{font-size:11px;font-weight:800;color:var(--ink);letter-spacing:.3px}
.wwd-text .lead{font-size:6.5px;font-weight:700;margin:6px 0 4px}
.wwd-text p{font-size:5.3px;color:var(--muted);margin-bottom:4px}

/* services */
.services{position:absolute;left:0;top:600px;width:709px;height:195px;background:linear-gradient(180deg,var(--blue),var(--blue-dark));color:var(--white);text-align:center}
.services h2{font-size:11px;font-weight:700;padding-top:22px;letter-spacing:.5px}
.services .rule{width:40px;height:1px;background:rgba(255,255,255,.5);margin:6px auto 0}
.service-list{display:flex;justify-content:center;gap:18px;margin-top:18px}
.service{width:100px}
.service-icon{width:42px;height:42px;border-radius:50%;background:var(--white);margin:0 auto;display:flex;align-items:center;justify-content:center;border:3px solid rgba(255,255,255,.4);background-clip:padding-box}
.service h4{font-size:6px;font-weight:700;margin-top:8px}
.service p{font-size:5px;opacity:.85;margin-top:3px}

/* news & testimonials */
.news-row{position:absolute;left:122px;top:805px;width:466px;height:140px;display:flex;gap:20px}
.col{flex:1}
.col-title{font-size:10px;font-weight:800;color:var(--blue);border-bottom:1px solid var(--line);padding-bottom:4px}
.news-item{display:flex;gap:6px;margin-top:8px}
.news-date{width:22px;height:24px;background:var(--blue);color:var(--white);font-size:5px;text-align:center;font-weight:700;padding-top:4px;flex:none}
.news-date b{display:block;font-size:8px}
.news-item h5{font-size:6px;font-weight:700}
.news-item p{font-size:5px;color:var(--muted)}
.quote{margin-top:8px;background:var(--page);padding:8px;font-size:5.3px;color:var(--muted);position:relative}
.quote-person{display:flex;align-items:center;gap:6px;margin-top:8px}
.avatar{width:18px;height:18px;border-radius:50%;background:linear-gradient(135deg,#c9b9a8,#7c6a5c)}
.quote-person b{font-size:5.5px;color:var(--ink)}
.slider-dots{position:absolute;right:8px;bottom:-12px;display:flex;gap:3px}
.slider-dots i{width:4px;height:4px;border-radius:50%;background:var(--line)}
.slider-dots i.on{background:var(--blue)}

/* partners */
.partners{position:absolute;left:0;top:945px;width:709px;height:45px;background:var(--page);border-top:1px solid var(--line)}
.partners p{font-size:5px;text-align:center;color:var(--muted);padding-top:4px}
.partner-list{display:flex;justify-content:center;gap:22px;margin-top:5px}
.partner-badge{width:48px;height:18px;background:#b8bec7;border-radius:2px}

/* footer */
.site-footer{position:absolute;left:0;top:990px;width:709px;height:172px;background:var(--footer);color:#aab1ba}
.footer-inner{position:absolute;left:122px;top:16px;width:466px;display:flex;gap:16px}
.footer-brand{width:150px}
.footer-brand .brand-name{color:var(--white);font-size:15px;width:auto}
.footer-brand h6{color:var(--white);font-size:7px;margin-top:18px}
.footer-brand p{font-size:5px;margin-top:3px}
.newsletter{display:flex;margin-top:6px}
.newsletter span{flex:1;height:12px;background:#3a404a}
.newsletter b{background:var(--red);color:var(--white);font-size:5px;padding:2px 6px;line-height:8px}
.footer-col{flex:1}
.footer-col h6{color:var(--white);font-size:7px;margin-bottom:6px}
.footer-col li{list-style:none;font-size:5.3px;line-height:10px}
.footer-bottom{position:absolute;left:0;top:1162px;width:709px;height:38px;background:var(--footer-bottom);color:#8c939c;font-size:5.5px}
.footer-bottom .copy{position:absolute;left:122px;top:14px}
.footer-bottom .follow{position:absolute;right:121px;top:11px;display:flex;align-items:center;gap:3px}
.follow-box{width:12px;height:12px;background:var(--blue);border-radius:1px}
</style>
</head>
<body>
<div class="page">

  <header class="site-header">
    <div class="brand">
      <span class="brand-mark"></span>
      <span class="brand-name">Liberty Ledger Tax</span>
    </div>
    <div class="top-contact">
      <svg width="8" height="8" viewBox="0 0 24 24"><path fill="#0355a3" d="M6.6 10.8a15.1 15.1 0 0 0 6.6 6.6l2.2-2.2a1 1 0 0 1 1-.25 11.4 11.4 0 0 0 3.6.57 1 1 0 0 1 1 1V20a1 1 0 0 1-1 1A17 17 0 0 1 3 4a1 1 0 0 1 1-1h3.5a1 1 0 0 1 1 1c0 1.25.2 2.45.57 3.57a1 1 0 0 1-.25 1z"/></svg>
      <span>(555) 014-2290</span>
      <span class="social-dot"></span><span class="social-dot"></span><span class="social-dot"></span>
    </div>
    <nav class="main-nav">
      <a class="active">HOME</a><a>ABOUT US</a><a>SERVICES</a><a>NEWS</a><a>TESTIMONIALS</a><a>CONTACT US</a>
    </nav>
  </header>

  <section class="hero" role="img" aria-label="Photo of hands reviewing tax documents and charts on a tablet">
    <div class="hero-welcome">
      <h1>WELCOME TO <span>LIBERTY LEDGER TAX</span></h1>
      <p>Lorem ipsum dolor sit amet, consectetur adipiscing elit, sed do eiusmod tempor incididunt ut labore et dolore magna aliqua.</p>
    </div>
    <div class="hero-arrow prev"><svg width="10" height="16" viewBox="0 0 10 16"><path d="M8 1 2 8l6 7" stroke="#fff" stroke-width="2" fill="none"/></svg></div>
    <div class="hero-arrow next"><svg width="10" height="16" viewBox="0 0 10 16"><path d="m2 1 6 7-6 7" stroke="#fff" stroke-width="2" fill="none"/></svg></div>
  </section>

  <section class="features">
    <article class="feature">
      <div class="feature-photo" role="img" aria-label="Photo of a business meeting with documents" style="background:linear-gradient(135deg,#dfe4ea,#8e9bab)"></div>
      <div class="feature-caption">LOREM IPSUM<small>Lorem ipsum dolor sit amet</small></div>
    </article>
    <article class="feature is-blue">
      <svg width="22" height="22" viewBox="0 0 24 24"><rect x="4" y="4" width="16" height="16" rx="2" fill="none" stroke="#fff" stroke-width="1.6"/><path d="M8 12h8M8 8h8M8 16h5" stroke="#fff" stroke-width="1.6"/></svg>
      <h3>LOREM IPSUM</h3>
      <p>Lorem ipsum dolor sit amet, consectetur adipiscing elit sed do eiusmod.</p>
      <span class="btn dark">READ MORE</span>
    </article>
    <article class="feature">
      <div class="feature-photo" role="img" aria-label="Photo of a calculator and financial charts" style="background:linear-gradient(135deg,#e8eef4,#9fb4c9)"></div>
      <div class="feature-caption">LOREM IPSUM<small>Lorem ipsum dolor sit amet</small></div>
    </article>
  </section>

  <section class="what-we-do">
    <div class="wwd-photo" role="img" aria-label="Photo of a smiling tax professional in an office"></div>
    <div class="wwd-text">
      <h2 class="section-title">WHAT WE DO</h2>
      <p class="lead">Lorem ipsum dolor sit amet consectetur adipiscing elit.</p>
      <p>Lorem ipsum dolor sit amet, consectetur adipiscing elit, sed do eiusmod tempor incididunt ut labore et dolore magna aliqua. Ut enim ad minim veniam, quis nostrud exercitation ullamco laboris nisi ut aliquip ex ea commodo consequat.</p>
      <p>Duis aute irure dolor in reprehenderit in voluptate velit esse cillum dolore eu fugiat nulla pariatur. Excepteur sint occaecat cupidatat non proident, sunt in culpa qui officia deserunt mollit anim id est laborum.</p>
      <p>Sed ut perspiciatis unde omnis iste natus error sit voluptatem accusantium doloremque laudantium totam rem aperiam.</p>
      <span class="btn">READ MORE</span>
    </div>
  </section>

  <section class="services">
    <h2>OUR SERVICES</h2>
    <div class="rule"></div>
    <div class="service-list">
      <div class="service">
        <div class="service-icon" style="background:var(--red)"><svg width="18" height="18" viewBox="0 0 24 24"><rect x="5" y="11" width="14" height="10" rx="1.5" fill="#fff"/><path d="M8 11V8a4 4 0 0 1 8 0v3" stroke="#fff" stroke-width="2" fill="none"/></svg></div>
        <h4>LOREM IPSUM DOLOR</h4>
        <p>Lorem ipsum dolor sit amet consectetur adipiscing elit sed do.</p>
      </div>
      <div class="service">
        <div class="service-icon" style="background:#2a7ad0"><svg width="18" height="18" viewBox="0 0 24 24"><rect x="3" y="4" width="18" height="12" rx="1" fill="none" stroke="#fff" stroke-width="2"/><path d="M9 20h6M12 16v4" stroke="#fff" stroke-width="2"/></svg></div>
        <h4>LOREM IPSUM DOLOR</h4>
        <p>Lorem ipsum dolor sit amet consectetur adipiscing elit sed do.</p>
      </div>
      <div class="service">
        <div class="service-icon" style="background:#2a7ad0"><svg width="18" height="18" viewBox="0 0 24 24"><circle cx="12" cy="8" r="4" fill="#fff"/><path d="M4 21a8 8 0 0 1 16 0z" fill="#fff"/></svg></div>
        <h4>LOREM IPSUM DOLOR</h4>
        <p>Lorem ipsum dolor sit amet consectetur adipiscing elit sed do.</p>
      </div>
      <div class="service">
        <div class="service-icon" style="background:#2a7ad0"><svg width="18" height="18" viewBox="0 0 24 24"><path d="M3 9h18l-2 11H5z" fill="#fff"/><path d="M8 9l4-6 4 6" stroke="#fff" stroke-width="2" fill="none"/></svg></div>
        <h4>LOREM IPSUM DOLOR</h4>
        <p>Lorem ipsum dolor sit amet consectetur adipiscing elit sed do.</p>
      </div>
    </div>
  </section>

  <section class="news-row">
    <div class="col">
      <h3 class="col-title">LATEST NEWS</h3>
      <div class="news-item">
        <div class="news-date"><b>12</b>JAN</div>
        <div><h5>Lorem ipsum dolor sit amet consectetur.</h5><p>Lorem ipsum dolor sit amet, consectetur adipiscing elit, sed do eiusmod tempor incididunt ut labore.</p></div>
      </div>
      <div class="news-item">
        <div class="news-date"><b>08</b>JAN</div>
        <div><h5>Lorem ipsum dolor sit amet consectetur.</h5><p>Lorem ipsum dolor sit amet, consectetur adipiscing elit, sed do eiusmod tempor incididunt ut labore.</p></div>
      </div>
    </div>
    <div class="col">
      <h3 class="col-title">TESTIMONIALS</h3>
      <div class="quote">
        Lorem ipsum dolor sit amet, consectetur adipiscing elit, sed do eiusmod tempor incididunt ut labore et dolore magna aliqua. Ut enim ad minim veniam, quis nostrud exercitation ullamco laboris nisi ut aliquip.
        <div class="quote-person"><div class="avatar" role="img" aria-label="Client portrait"></div><div><b>Lorem Ipsum</b><br>Happy Client</div></div>
        <div class="slider-dots"><i class="on"></i><i></i><i></i></div>
      </div>
    </div>
  </section>

  <section class="partners">
    <p>We are Participating Providers for the Insurance Plans</p>
    <div class="partner-list">
      <span class="partner-badge" role="img" aria-label="Partner badge"></span>
      <span class="partner-badge" role="img" aria-label="Partner badge"></span>
      <span class="partner-badge" role="img" aria-label="Partner badge"></span>
      <span class="partner-badge" role="img" aria-label="Partner badge"></span>
      <span class="partner-badge" role="img" aria-label="Partner badge"></span>
    </div>
  </section>

  <footer class="site-footer">
    <div class="footer-inner">
      <div class="footer-brand">
        <span class="brand-name">Liberty Ledger Tax</span>
        <h6>Newsletter</h6>
        <p>Sign up for our latest news and updates.</p>
        <div class="newsletter"><span></span><b>SEND</b></div>
      </div>
      <div class="footer-col"><h6>Main menu</h6><ul><li>Home</li><li>About Us</li><li>Services</li><li>News</li><li>Contact</li></ul></div>
      <div class="footer-col"><h6>Main menu</h6><ul><li>Tax Filing</li><li>Planning</li><li>Payroll</li><li>Audits</li><li>Refunds</li></ul></div>
      <div class="footer-col"><h6>Contact us</h6><ul><li>120 Example Avenue</li><li>Springfield, ST 00000</li><li>(555) 014-2290</li><li>info@libertyledger.example</li></ul></div>
    </div>
  </footer>
  <div class="footer-bottom">
    <span class="copy">© 2014 Liberty Ledger Tax. All rights reserved | Site by PIXELHARBOR</span>
    <div class="follow">Follow Us <span class="follow-box"></span><span class="follow-box"></span><span class="follow-box"></span><span class="follow-box"></span><span class="follow-box"></span></div>
  </div>

</div>
</body>
</html>
```